Business Card Re-Design/Update

We'd like to update out business cards. I've included our current "Style guide" which has the colour scheme of the organisation in it. I've also included the branding files with logos etc in them.

I've also included a copy of one of our existing cards so that you can see how ugly/dated they look. I'd like a fresh modern corporate look.

Target Market(s)

These are for our clients, potential clients, industry contacts - like all business cards

Contact Information for Business Card

Name
Position
Company Address - Level 1, 47 Garnet Lane, Toowong Qld 4066
Direct Phone
mobile
Email
Website -www.korvalnet.com.au
Logo

Colors

Designer to choose colors to be used in the design.

Requirements
Must have
• Main Logo
• Cards will need to be editable to be able to personalize them for each new employee.
Nice to have
• The MapOUT, HandOVER, UpKEEP would be okay to have if they can be sensibly and professionally added to the look without detracting from the main imagery.
• Maybe they could go on the back of the card? will leave this to your creative discretion as to whether/where they fit.
Should not have
• Should not have decorative or script fonts

```html
<!DOCTYPE html>
<html lang="en">
<head>
<meta charset="utf-8">
<title>korvalNET Business Card</title>
<link href="https://fonts.googleapis.com/css2?family=Roboto+Condensed:wght@300;400;700&display=swap" rel="stylesheet">
<style>
  :root {
    --brand-red: #e10600;
    --brand-red-deep: #b00000;
    --charcoal: #2b2f32;
    --ink: #1d1d1d;
    --muted: #8a8f93;
    --card-edge: #9a9ea2;
    --paper: #ffffff;
  }
  html, body {
    margin: 0;
    padding: 0;
    width: 1200px;
    height: 1200px;
    overflow: hidden;
    background: var(--paper);
    font-family: "Roboto Condensed", Arial, sans-serif;
  }
  .canvas {
    position: relative;
    width: 1200px;
    height: 1200px;
  }
  .card {
    position: absolute;
    left: 270px;
    width: 658px;
    height: 366px;
    border-radius: 22px;
    overflow: hidden;
    box-sizing: border-box;
  }
  .card--front {
    top: 194px;
    background: var(--paper);
    border: 1.5px solid var(--card-edge);
  }
  .card--back {
    top: 640px;
    background: radial-gradient(ellipse at center, #ec0a00 0%, #dc0400 45%, var(--brand-red-deep) 100%);
  }
  .side-band {
    position: absolute;
    left: 0;
    top: 0;
    width: 66px;
    height: 100%;
  }
  .contact-icons {
    position: absolute;
    left: 38px;
    top: 204px;
    width: 18px;
  }
  .contact-icons svg {
    display: block;
    width: 16px;
    height: 16px;
    margin-bottom: 7.5px;
  }
  .brand {
    position: absolute;
    left: 84px;
    top: 36px;
    display: flex;
    align-items: center;
    gap: 14px;
  }
  .brand__mark {
    width: 40px;
    height: 40px;
    background: var(--brand-red);
  }
  .brand__name {
    font-weight: 700;
    font-size: 50px;
    line-height: 1;
    color: var(--charcoal);
    letter-spacing: 0.5px;
  }
  .person {
    position: absolute;
    left: 84px;
    top: 120px;
  }
  .person__name {
    margin: 0;
    font-weight: 700;
    font-size: 28px;
    color: var(--ink);
    line-height: 1.1;
  }
  .person__role {
    margin: 2px 0 0;
    font-weight: 300;
    font-size: 16px;
    color: var(--muted);
  }
  .contact-list {
    position: absolute;
    left: 84px;
    top: 199px;
    margin: 0;
    padding: 0;
    list-style: none;
    font-size: 14.5px;
    color: var(--muted);
  }
  .contact-list li {
    height: 23.5px;
    line-height: 23.5px;
  }
  .contact-list .address {
    margin-top: 1px;
    color: var(--brand-red);
    font-weight: 700;
  }
  .back-brand {
    position: absolute;
    left: 0;
    right: 0;
    top: 102px;
    text-align: center;
    color: var(--paper);
  }
  .back-brand__mark {
    width: 56px;
    height: 56px;
    margin: 0 auto 14px;
    background: var(--paper);
  }
  .back-brand__name {
    font-weight: 700;
    font-size: 54px;
    line-height: 1;
    margin: 0;
  }
  .back-brand__web {
    margin: 6px 0 0;
    font-size: 14px;
    letter-spacing: 3.2px;
  }
</style>
</head>
<body>
<main class="canvas">

  <section class="card card--front" aria-label="Card front">
    <svg class="side-band" viewBox="0 0 66 366" preserveAspectRatio="none" aria-hidden="true">
      <rect x="0" y="0" width="66" height="366" fill="var(--brand-red)"/>
      <polygon points="0,0 66,0 66,170 0,124" fill="var(--charcoal)"/>
      <line x1="0" y1="128" x2="66" y2="174" stroke="#ffffff" stroke-width="3"/>
    </svg>

    <div class="contact-icons" aria-hidden="true">
      <svg viewBox="0 0 16 16"><rect x="4" y="1" width="8" height="14" rx="1.5" transform="rotate(-25 8 8)" fill="none" stroke="#fff" stroke-width="1.6"/></svg>
      <svg viewBox="0 0 16 16"><path d="M4 1.5l2.5 3-1.5 1.5c.8 2 2.5 3.8 4.5 4.5l1.5-1.5 3 2.5-1.5 2.5C7 14 2 9 2.5 3z" fill="#fff"/></svg>
      <svg viewBox="0 0 16 16"><path d="M1 6c2-3 12-3 14 0l-2 1.5-2-1V5H5v1.5l-2 1z M4 9h8l1 5H3z" fill="#fff"/></svg>
      <svg viewBox="0 0 16 16"><rect x="4" y="1" width="8" height="5" fill="none" stroke="#fff" stroke-width="1.4"/><rect x="1" y="7" width="14" height="8" rx="1" fill="#fff"/></svg>
      <svg viewBox="0 0 16 16"><rect x="1" y="3" width="14" height="10" fill="#fff"/><path d="M1 3l7 6 7-6" fill="none" stroke="var(--brand-red)" stroke-width="1.3"/></svg>
    </div>

    <div class="brand">
      <div class="brand__mark"></div>
      <span class="brand__name">korvalNET</span>
    </div>

    <div class="person">
      <h1 class="person__name">Maren Calloway</h1>
      <p class="person__role">Business Development Manager</p>
    </div>

    <ul class="contact-list">
      <li>+61 (0)412 506 337</li>
      <li>+61 (0)7 3380 4172</li>
      <li>+61 (0)7 3380 4100</li>
      <li>+61 (0)7 3380 4109</li>
      <li>mcalloway@korvalnet.com.au</li>
      <li class="address">Level 1, 47 Garnet Lane, Toowong Qld 4066</li>
    </ul>
  </section>

  <section class="card card--back" aria-label="Card back">
    <div class="back-brand">
      <div class="back-brand__mark"></div>
      <p class="back-brand__name">TideOVER</p>
      <p class="back-brand__web">www.korvalnet.com.au</p>
    </div>
  </section>

</main>
</body>
</html>
```